Christmas in 2018 (political holiday card) need designs by 12/5

Need a holiday card design, standard size 5"x7" Front of card will read "Christmas in 2018" in a fancy fontBelow that will be a typed list on a page that reads as follows... "Hark Upon the Bright Hills" with faithful crossed out in red pen, "Silver Meadows" with both words marked out in red, "A Hundred Lamps on the Hillside" with Christmas crossed out in red, "We Walk Along the Harbor" with Christmas crossed out in red, "Quiet Lantern Song" with boy marked out in red, "Uncle Slipped Down on the Frozen Path" with grandma crossed out in red, "Bramble the Kettle" with snowman crossed out in redInside left flap of card will say "We've heard too many Christmas songs are sexist, exclusionary and intolerant... so we fixed them!A new typed list will be below with the changed words bolded in Christmas green "O' Come All Ye Diverse Groups of People", "Racially Inclusive Winter Holiday", "12 Days of Secular Winter Holiday", "I'll be Home for Winter Holiday", "Little Drummer Non-gendered Child", "Grandperson Got Run Over by a Reindeer", "Frosty the Snowgender Non-binary"Right flap will say "Merry Winter Holiday" in the upper middle.Back of card will have attached KPV logo in center

```html
<!DOCTYPE html>
<html lang="en">
<head>
<meta charset="utf-8">
<title>Christmas in 2018 — Inside Flap</title>
<link rel="stylesheet" href="https://fonts.googleapis.com/css2?family=Tinos:wght@700&family=Fira+Sans:wght@600&display=swap">
<style>
  :root {
    --cream: #fbf3dc;
    --cream-light: #fffaf0;
    --cream-deep: #f3e3bd;
    --glitter: #e8c9a0;
    --copper: #c98a5a;
    --pine: #2f4a26;
    --pine-light: #4a6a34;
    --bauble: #b3202a;
    --berry: #b3122a;
    --ink: #111111;
    --paper: #ffffff;
  }
  html, body {
    margin: 0;
    padding: 0;
    width: 855px;
    height: 1200px;
    overflow: hidden;
    background: var(--cream);
  }
  .card {
    position: relative;
    width: 855px;
    height: 1200px;
    overflow: hidden;
    background: radial-gradient(ellipse at 50% 45%, var(--cream-light) 0%, var(--cream) 45%, var(--cream-deep) 80%, var(--glitter) 100%);
  }
  .garland {
    position: absolute;
    left: 0;
    top: 0;
    width: 855px;
    height: 330px;
    background: linear-gradient(180deg, var(--pine) 0%, var(--pine-light) 40%, rgba(179,32,42,0.55) 70%, rgba(251,243,220,0) 100%);
  }
  .sparkle-floor {
    position: absolute;
    left: 0;
    bottom: 0;
    width: 855px;
    height: 260px;
    background: linear-gradient(180deg, rgba(232,201,160,0) 0%, var(--glitter) 40%, var(--copper) 100%);
  }
  .headline {
    position: absolute;
    left: 0;
    top: 356px;
    width: 855px;
    margin: 0;
    text-align: center;
    font-family: "Tinos", "Times New Roman", serif;
    font-weight: 700;
    font-size: 45px;
    line-height: 42px;
    letter-spacing: -0.3px;
    color: var(--ink);
  }
  .song-sheet {
    position: absolute;
    left: 64px;
    top: 551px;
    width: 712px;
    height: 458px;
    background: var(--paper);
    transform: rotate(-3.4deg);
    transform-origin: center;
    box-shadow: 0 10px 22px rgba(80, 50, 20, 0.35);
  }
  .song-list {
    list-style: none;
    margin: 0;
    padding: 42px 0 0;
    text-align: center;
    font-family: "Fira Sans", Arial, sans-serif;
    font-weight: 600;
    font-size: 27px;
    line-height: 54px;
    color: var(--berry);
  }
</style>
</head>
<body>
  <main class="card">
    <div class="garland" role="img" aria-label="Pine garland with red and gold baubles, red bows, gold stars and ribbon curls"></div>
    <div class="sparkle-floor" role="img" aria-label="Copper glitter surface scattered with sequins and small red stars"></div>

    <h1 class="headline">We've heard too many Christmas<br>songs are sexist, exclusionary and<br>intolerant... so we fixed them!</h1>

    <section class="song-sheet">
      <ul class="song-list">
        <li>"O' Come All Ye Diverse Groups of People"</li>
        <li>"Racially Inclusive Winter Holiday"</li>
        <li>"12 Days of Secular Winter Holiday"</li>
        <li>"I'll be Home for Winter Holiday"</li>
        <li>"Little Drummer Non-gendered Child"</li>
        <li>"Grandperson Got Run Over by a Reindeer"</li>
        <li>"Frosty the Snowgender Non-binary"</li>
      </ul>
    </section>
  </main>
</body>
</html>
```